Hvac and insulation company needs good looking business card design

We are hvac and insulation company and looking for a new business cards that look to today standards designs

Target Market(s)

homeowners

Industry/Entity Type

Hvac

Contact Information for Business Card

Name: Doran Velkisk
Home comfort consultant
address: 4827 Brimwood Ct #215 Oakland, CA 94619
office: 888-731-5096
cell: 510-874-3190
Lic.# 648215
Email: doran@quorvix-hvac.example
Web: quorvix-hvac.example

Requirements
Must have
• clean and sleek look
Nice to have
• simple with a clean look
Should not have
• to busy business card

```html
<!DOCTYPE html>
<html lang="en">
<head>
<meta charset="utf-8">
<title>Quorvix – Business Card</title>
<link href="https://fonts.googleapis.com/css2?family=Open+Sans:wght@400;600;700&family=Oswald:wght@600&display=swap" rel="stylesheet">
<style>
  :root {
    --backdrop: #3a3a3b;
    --card: #232323;
    --orange: #f0900f;
    --white: #f2f2f2;
    --muted: #9a9a9a;
  }
  * { box-sizing: border-box; margin: 0; padding: 0; }
  html, body { width: 1200px; height: 900px; overflow: hidden; }
  body {
    background: var(--backdrop);
    font-family: "Open Sans", sans-serif;
    display: flex;
    flex-direction: column;
    align-items: center;
    justify-content: center;
    gap: 36px;
  }
  .card {
    position: relative;
    width: 700px;
    height: 400px;
    background: var(--card);
    box-shadow: 0 10px 30px rgba(0,0,0,.35);
    overflow: hidden;
  }
  .brand {
    display: flex;
    align-items: center;
    gap: 14px;
  }
  .brand-square {
    width: 34px;
    height: 34px;
    background: var(--orange);
  }
  .brand-name {
    font-weight: 700;
    color: var(--orange);
    letter-spacing: 1px;
    line-height: 1;
  }

  /* Front */
  .card-front .brand {
    position: absolute;
    left: 50%;
    top: 150px;
    transform: translateX(-50%);
  }
  .card-front .brand-name { font-size: 52px; }
  .front-web {
    position: absolute;
    left: 0; right: 0;
    bottom: 48px;
    text-align: center;
    font-size: 16px;
    letter-spacing: 1px;
    color: var(--white);
  }
  .front-web .accent, .contact-web .accent { color: var(--orange); }

  /* Back */
  .card-back .brand {
    position: absolute;
    left: 48px;
    top: 158px;
  }
  .card-back .brand-square { width: 44px; height: 44px; }
  .card-back .brand-name { font-size: 56px; }
  .divider {
    position: absolute;
    left: 372px;
    top: 66px;
    width: 2px;
    height: 250px;
    background: var(--white);
  }
  .details {
    position: absolute;
    left: 398px;
    top: 62px;
    right: 20px;
    color: var(--white);
  }
  .person-name {
    font-family: "Oswald", sans-serif;
    font-size: 34px;
    font-weight: 600;
    text-transform: uppercase;
    letter-spacing: .5px;
    line-height: 1.1;
  }
  .person-title {
    font-size: 15px;
    font-weight: 600;
    color: var(--orange);
    margin-bottom: 18px;
  }
  .address, .license {
    font-size: 15px;
    line-height: 1.45;
    letter-spacing: 1px;
  }
  .license { margin: 6px 0 10px; }
  .contact-list { list-style: none; }
  .contact-list li {
    display: flex;
    align-items: center;
    gap: 14px;
    font-size: 15px;
    letter-spacing: .5px;
    line-height: 1.8;
  }
  .contact-list svg {
    width: 16px;
    height: 16px;
    flex: none;
    fill: none;
    stroke: var(--orange);
    stroke-width: 1.8;
    stroke-linecap: round;
    stroke-linejoin: round;
  }
  .bottom-band {
    position: absolute;
    left: 0; right: 0; bottom: 0;
    height: 12px;
    background: var(--orange);
  }
</style>
</head>
<body>

  <section class="card card-front">
    <div class="brand">
      <span class="brand-square"></span>
      <span class="brand-name">quorvix</span>
    </div>
    <p class="front-web">www.<span class="accent">quorvix-hvac</span>.example</p>
  </section>

  <section class="card card-back">
    <div class="brand">
      <span class="brand-square"></span>
      <span class="brand-name">quorvix</span>
    </div>
    <div class="divider"></div>
    <div class="details">
      <h1 class="person-name">Doran Velkisk</h1>
      <p class="person-title">Home comfort consultant</p>
      <p class="address">4827 Brimwood Ct #215<br>Oakland, CA 94619</p>
      <p class="license">Lic #648215</p>
      <ul class="contact-list">
        <li>
          <svg viewBox="0 0 16 16"><rect x="4" y="1.5" width="8" height="13" rx="1.5"/><line x1="7" y1="12" x2="9" y2="12"/></svg>
          888-731-5096
        </li>
        <li>
          <svg viewBox="0 0 16 16"><path d="M3 2.5l3 .5 1 3-1.8 1.2a8 8 0 0 0 3.6 3.6L10 9l3 1 .5 3-1.5 1.5C7 14 2 9 1.5 4z"/></svg>
          510-874-3190
        </li>
        <li>
          <svg viewBox="0 0 16 16"><rect x="1.5" y="3.5" width="13" height="9" rx="1"/><polyline points="1.5,4 8,9 14.5,4"/></svg>
          doran@quorvix-hvac.example
        </li>
        <li class="contact-web">
          <svg viewBox="0 0 16 16"><circle cx="8" cy="8" r="6.5"/><ellipse cx="8" cy="8" rx="2.8" ry="6.5"/><line x1="1.5" y1="8" x2="14.5" y2="8"/></svg>
          <span>www.<span class="accent">quorvix-hvac</span>.example</span>
        </li>
      </ul>
    </div>
    <div class="bottom-band"></div>
  </section>

</body>
</html>
```